WISP Laser Hair Removal Information Flyer

I’m looking to have a (tri-fold?) flyer created to provide some information about my laser Hair Removal business. I would like to include my logo (uploaded) as well as the following information:

WISP Laser Hair Removal Prices:

FACE
Upper Lip: $35
Chin: $35
Cheeks: $35
Full Face (Lip/Chin/Cheeks) - $100
Middle Brow: $25

UPPER BODY (above waist)
Underarm: $75
Chest: $150
Full Arm: $150
1/2 Arm: $100
Areola: $50
Full Back: $250
Shoulders: $75
Full Hands w/ Fingers: $50
Fingers only: $25

LOWER BODY (below waist)
Full Leg: $300
Upper Leg: $175
Lower Leg: $150
Stomach: $150
Navel and Navel Line: $50
Navel and Lower Abdomen: $100
Lower Back: $100
Classic Bikini: $75
Deep Bikini or Brazilian: $125
Buttocks: $100
Between cheeks: $75
Full Feet w/ Toes: $50
Toes Only: $25

Women (common combinations)
Full Arm w/ Underarm: $200
Full Leg w/ Classic Bikini: $350
Full Leg w/ Deep Bikini or Brazilian: $375
Classic Bikini w/ Inner Thigh: $100
Deep Bikini or Brazilian w/ Inner Thigh: $150

Men (common areas and combinations)
1/2 Face & Neck (front): $100
Cheeks & Neck (front): $75
Full Neck: $75
Nape of Neck: $50
Shoulders: $75
Full Back: $250
Full Back & Full Neck: $300
Neck (nape) and Shoulders: $100
Full Back, Neck and Buttocks: $375

Laser Hair Removal is an affordable, safe and effective way to treat unwanted hair - permanently!

WISP uses the Corvana GlideMark(TM) Diode Laser - the Gold Standard in Laser Hair Removal!

Wisp Laser Hair Removal with the Corvana GlideMark (TM):

The Corvana aesthetic division is a worldwide leader in energy-based aesthetic devices with presence in over 100 countries, as a pioneer in the field of aesthetic medicine. GlideMark (TM) is FDA approved and uses clinically proven diode laser technology to permanently remove unwanted hair comfortably, safely and effectively, for all skin colours and types - even with a tan.

How It works:
The GlideMark (TM) is able to stop the growth of unwanted hair permanently, by delivering high-energy pulses to the hair follicle. This is achieved by targeting the melanin inside the follicle and heating it up until follicle damage occurs. Treatments are made comfortable by the patented Frost Nib Integrated Technology; a system that continuously cools the skin of the area being treated.

What to expect:
Laser Hair Removal requires multiple sessions (typically between 6 - 8), spaced approximately 6 weeks between each session.

For more information, visit us at
www.wisplaser-example.ca
IG:
@wisplaserdemo

Find us on Facebook - WISP Laser Demo

Wisp is proudly partnered with the Maplegrove Aesthetic Clinic
4860 Tollway Crescent, Suite 115
London, ON

Contact WISP today for your complimentary consultation!

Marisol@wisplaser-example.ca
555-013-8826

* if the uploaded logo is not the right format, please let me know and I will upload a new file *

```html
<!DOCTYPE html>
<html lang="en">
<head>
<meta charset="utf-8">
<title>WISP Laser Hair Removal – Tri-fold Flyer</title>
<link href="https://fonts.googleapis.com/css2?family=Open+Sans:wght@300;400;600&family=Raleway:wght@300&display=swap" rel="stylesheet">
<style>
:root{
  --stage:#e4e4e4;
  --grey:#7b7b7d;
  --grey-mid:#a3a3a5;
  --grey-dark:#6c6c6e;
  --pink:#d7a499;
  --pink-soft:#f1ddd7;
  --white:#ffffff;
  --ink:#6f6f71;
  --photo-skin:#d9c3b4;
  --photo-light:#f3ece7;
}
*{box-sizing:border-box;margin:0;padding:0}
html,body{width:1200px;height:2400px;overflow:hidden}
body{background:var(--stage);font-family:"Open Sans",Arial,sans-serif;color:var(--ink);position:relative}

.spread{position:absolute;left:50px;width:1100px;height:850px;display:grid;grid-template-columns:repeat(3,1fr);background:var(--white);box-shadow:0 10px 30px rgba(0,0,0,.12)}
.spread--outside{top:190px}
.spread--inside{top:1300px}
.panel{position:relative;overflow:hidden;height:850px}
.panel + .panel{border-left:1px solid rgba(0,0,0,.05)}
.panel-bg{position:absolute;inset:0;width:100%;height:100%}

.photo{position:absolute;background:linear-gradient(160deg,var(--photo-light),var(--photo-skin))}
.photo--round{border-radius:50%;border:4px solid var(--white);box-shadow:0 0 0 2px var(--pink)}

/* brand */
.brand{position:absolute;text-align:center;font-family:"Raleway",Arial,sans-serif;font-weight:300;color:var(--pink);line-height:1}
.brand__name{display:block;font-size:64px;letter-spacing:6px}
.brand__tag{display:block;font-size:17px;letter-spacing:3px;margin-top:6px}

/* cover */
.cover .brand{top:48px;left:0;right:0}
.cover .photo{top:170px;left:0;right:0;height:470px}
.cover__foot{position:absolute;left:0;right:0;bottom:70px;text-align:center;color:var(--white)}
.cover__title{color:var(--pink);font-size:16px;letter-spacing:1px;margin-bottom:14px;text-transform:uppercase}
.cover__info{font-size:17px;line-height:1.5}

/* back panel */
.back{background:var(--grey-mid);color:var(--white)}
.back .map{position:absolute;top:60px;left:50%;width:150px;height:150px;margin-left:-75px;border-radius:50%;background:linear-gradient(135deg,#eef3e4,#c9dcb5);border:4px solid var(--white);box-shadow:0 0 0 2px var(--pink)}
.back__contact{position:absolute;top:250px;left:30px;right:30px;text-align:center;font-size:16px;line-height:1.55}
.back__contact p + p{margin-top:18px}
.back .brand{bottom:110px;left:0;right:0}
.back__url{position:absolute;bottom:60px;left:0;right:0;text-align:center;font-size:16px;color:var(--white)}

/* info flap */
.flap__body{position:absolute;top:40px;left:30px;right:28px;font-size:12.2px;line-height:1.5}
.flap h2,.section-title{font-weight:400;color:var(--pink);font-size:15px;margin:0 0 6px}
.flap p{margin-bottom:14px;text-align:justify}
.flap .photo--round.legs{left:34px;top:612px;width:92px;height:92px}
.flap .photo--round.face{left:136px;top:606px;width:92px;height:92px}
.flap__expect{position:absolute;left:30px;right:28px;top:730px;color:var(--white);font-size:12px;line-height:1.5}
.flap__expect h2{color:var(--pink-soft);font-size:14px}

/* price lists */
.pill{display:inline-block;background:var(--pink);color:var(--white);font-size:14px;letter-spacing:.5px;padding:5px 40px 5px 26px;border-radius:0 20px 20px 0;margin:0 0 10px -30px;text-transform:uppercase}
.prices{list-style:none;font-size:13px;line-height:1.62}
.prices li{display:flex;align-items:baseline}
.prices li::after{content:"";order:1;flex:1;border-bottom:1px dotted currentColor;margin:0 4px;opacity:.7}
.prices .price{order:2}

.price-panel--face{background:var(--grey);color:var(--white)}
.price-panel--face .content{position:absolute;top:40px;left:30px;right:30px}
.price-panel--face .prices + .pill{margin-top:26px}
.price-panel--face .photo{left:0;right:0;bottom:0;height:240px}

.price-panel--lower .content{position:absolute;top:34px;left:30px;right:30px}
.price-panel--lower .pill{background:none;color:var(--pink);padding:0;margin:0 0 6px}
.price-panel--lower .photo{left:0;right:0;top:450px;height:190px}
.price-panel--lower .combos{position:absolute;top:650px;left:30px;right:30px}
.price-panel--lower .combos .section-title{text-align:center}

.price-panel--men{background:var(--grey);color:var(--white)}
.price-panel--men .photo{left:0;right:0;top:0;height:290px}
.price-panel--men .content{position:absolute;top:320px;left:30px;right:30px}
.price-panel--men .pill{font-size:12.5px;text-transform:none;padding-right:20px}
.men__note{margin-top:26px;font-size:12.5px;line-height:1.55}
.men__note p + p{margin-top:12px}
.men__url{margin-top:14px;color:var(--pink);font-size:13px}
</style>
</head>
<body>

<!-- Outside of the tri-fold -->
<section class="spread spread--outside">

  <article class="panel flap">
    <svg class="panel-bg" viewBox="0 0 367 850" preserveAspectRatio="none" aria-hidden="true">
      <path d="M0 700 Q180 640 367 690 L367 850 L0 850 Z" fill="var(--grey)"/>
      <path d="M0 690 Q180 630 367 680" fill="none" stroke="var(--pink)" stroke-width="5"/>
    </svg>
    <div class="flap__body">
      <h2>Wisp Laser Hair Removal with the Corvana GlideMark (TM):</h2>
      <p>The Corvana aesthetic division is a worldwide leader in energy-based aesthetic devices with presence in over 100 countries, as a pioneer in the field of aesthetic medicine. GlideMark (TM) is FDA approved and uses clinically proven diode laser technology to permanently remove unwanted hair comfortably, safely and effectively, for all skin colours and types - even with a tan.</p>
      <h2>How It works:</h2>
      <p>The GlideMark (TM) is able to stop the growth of unwanted hair permanently, by delivering high-energy pulses to the hair follicle. This is achieved by targeting the melanin inside the follicle and heating it up until follicle damage occurs. Treatments are made comfortable by the patented Frost Nib Integrated Technology; a system that continuously cools the skin of the area being treated.</p>
    </div>
    <div class="photo photo--round legs" role="img" aria-label="Photo of smooth legs"></div>
    <div class="photo photo--round face" role="img" aria-label="Photo of a woman touching her cheek"></div>
    <div class="flap__expect">
      <h2>What to expect:</h2>
      <p>Laser Hair Removal requires multiple sessions (typically between 6 - 8), spaced approximately 6 weeks between each session.</p>
    </div>
  </article>

  <article class="panel back">
    <svg class="panel-bg" viewBox="0 0 367 850" preserveAspectRatio="none" aria-hidden="true">
      <path d="M0 610 Q180 560 367 600 L367 850 L0 850 Z" fill="var(--grey)"/>
      <path d="M0 600 Q180 550 367 590" fill="none" stroke="var(--pink)" stroke-width="5"/>
    </svg>
    <div class="map" role="img" aria-label="Map showing the clinic location"></div>
    <div class="back__contact">
      <p>Maplegrove Aesthetic Clinic<br>4860 Tollway Crescent,<br>Suite 115<br>London, Ontario A1A 1A1</p>
      <p>For more information, visit us at<br>www.wisplaser-example.ca<br>IG: @wisplaserdemo</p>
      <p>Find us on Facebook:<br>WISP Laser Demo</p>
    </div>
    <div class="brand"><span class="brand__name">WISP</span><span class="brand__tag">LASER HAIR REMOVAL</span></div>
    <p class="back__url">www.wisplaser-example.ca</p>
  </article>

  <article class="panel cover">
    <div class="brand"><span class="brand__name">WISP</span><span class="brand__tag">LASER HAIR REMOVAL</span></div>
    <div class="photo" role="img" aria-label="Portrait of a woman with long brown hair"></div>
    <svg class="panel-bg" viewBox="0 0 367 850" preserveAspectRatio="none" aria-hidden="true">
      <path d="M0 660 Q220 650 367 480 L367 850 L0 850 Z" fill="var(--grey)"/>
      <path d="M0 650 Q215 640 367 470" fill="none" stroke="var(--pink)" stroke-width="5"/>
      <path d="M0 168 L367 168" stroke="var(--pink-soft)" stroke-width="3"/>
    </svg>
    <div class="cover__foot">
      <p class="cover__title">WISP Laser Hair Removal Prices</p>
      <p class="cover__info">For more information, visit us at<br>www.wisplaser-example.ca</p>
    </div>
  </article>
</section>

<!-- Inside of the tri-fold -->
<section class="spread spread--inside">

  <article class="panel price-panel--face">
    <div class="content">
      <h2 class="pill">Face</h2>
      <ul class="prices">
        <li>Upper Lip<span class="price">$35</span></li>
        <li>Chin<span class="price">$35</span></li>
        <li>Cheeks<span class="price">$35</span></li>
        <li>Full Face (Lip/Chin/Cheeks)<span class="price">$100</span></li>
        <li>Middle Brow<span class="price">$25</span></li>
      </ul>
      <h2 class="pill">Upper Body (above waist)</h2>
      <ul class="prices">
        <li>Underarm<span class="price">$75</span></li>
        <li>Chest<span class="price">$150</span></li>
        <li>Full Arm<span class="price">$150</span></li>
        <li>1/2 Arm<span class="price">$100</span></li>
        <li>Areola<span class="price">$50</span></li>
        <li>Full Back<span class="price">$250</span></li>
        <li>Shoulders<span class="price">$75</span></li>
        <li>Full Hands w/ Fingers<span class="price">$50</span></li>
        <li>Fingers only<span class="price">$25</span></li>
      </ul>
    </div>
    <div class="photo" role="img" aria-label="Photo of a laser treatment on a client's underarm"></div>
    <svg class="panel-bg" viewBox="0 0 367 850" preserveAspectRatio="none" aria-hidden="true">
      <path d="M0 608 Q180 640 367 600 L367 610 Q180 652 0 618 Z" fill="var(--pink)"/>
    </svg>
  </article>

  <article class="panel price-panel--lower">
    <div class="content">
      <h2 class="pill">Lower Body (below waist)</h2>
      <ul class="prices">
        <li>Full Leg<span class="price">$300</span></li>
        <li>Upper Leg<span class="price">$175</span></li>
        <li>Lower Leg<span class="price">$150</span></li>
        <li>Stomach<span class="price">$150</span></li>
        <li>Navel and Navel Line<span class="price">$50</span></li>
        <li>Navel and Lower Abdomen<span class="price">$100</span></li>
        <li>Lower Back<span class="price">$100</span></li>
        <li>Classic Bikini<span class="price">$75</span></li>
        <li>Deep Bikini or Brazilian<span class="price">$125</span></li>
        <li>Buttocks<span class="price">$100</span></li>
        <li>Between cheeks<span class="price">$75</span></li>
        <li>Full Feet w/ Toes<span class="price">$50</span></li>
        <li>Toes Only<span class="price">$25</span></li>
      </ul>
    </div>
    <div class="photo" role="img" aria-label="Photo of a woman seated, showing smooth legs"></div>
    <div class="combos">
      <h2 class="section-title">Women (common combinations)</h2>
      <ul class="prices">
        <li>Full Arm w/ Underarm<span class="price">$200</span></li>
        <li>Full Leg w/ Classic Bikini<span class="price">$350</span></li>
        <li>Full Leg w/ Deep Bikini or Brazilian<span class="price">$375</span></li>
        <li>Classic Bikini w/ Inner Thigh<span class="price">$100</span></li>
        <li>Deep Bikini or Brazilian w/ Inner Thigh<span class="price">$150</span></li>
      </ul>
    </div>
  </article>

  <article class="panel price-panel--men">
    <div class="photo" role="img" aria-label="Photo of a relaxed client receiving facial laser treatment"></div>
    <svg class="panel-bg" viewBox="0 0 367 850" preserveAspectRatio="none" aria-hidden="true">
      <path d="M0 300 Q180 250 367 290 L367 280 Q180 238 0 290 Z" fill="var(--pink)"/>
    </svg>
    <div class="content">
      <h2 class="pill">Men (common areas and combinations)</h2>
      <ul class="prices">
        <li>1/2 Face &amp; Neck (front)<span class="price">$100</span></li>
        <li>Cheeks &amp; Neck (front)<span class="price">$75</span></li>
        <li>Full Neck<span class="price">$75</span></li>
        <li>Nape of Neck<span class="price">$50</span></li>
        <li>Shoulders<span class="price">$75</span></li>
        <li>Full Back<span class="price">$250</span></li>
        <li>Full Back &amp; Full Neck<span class="price">$300</span></li>
        <li>Neck (nape) and Shoulders<span class="price">$100</span></li>
        <li>Full Back, Neck and Buttocks<span class="price">$375</span></li>
      </ul>
      <div class="men__note">
        <p>Laser Hair Removal is an affordable, safe and effective way to treat unwanted hair - permanently!</p>
        <p>WISP uses the Corvana GlideMark(TM) Diode Laser - the Gold Standard in Laser Hair Removal!</p>
        <p class="men__url">www.wisplaser-example.ca</p>
      </div>
    </div>
  </article>
</section>

</body>
</html>
```